Invitation for Annual Banquet

We would like an invitation designed for our annual banquet that depicts a bridge. We need your creative talent to come up with a theme. We are wanting to project that we are building a bridge to the future: a better future, a more prosperous future. We would like our logo colors incorporated or at least compliment the logo. We will be incorporating the graphics into the program as well. The event details are as follows: The Board of Directors and staff cordially invite you to attend the 82nd Annual Gathering & Small Trade Fair ~ Monday, January 28, 2019 ~ 5:30 P.M. Social, 6:00 P. M. Dinner ~ Eastvale Chapel, 4819 Carson T Hale Hwy S, Whiteville ~ Please RSVP by January 21, 2019
Logo Text
I don't know exactly!!

```html
<!DOCTYPE html>
<html lang="en">
<head>
<meta charset="utf-8">
<title>82nd Annual Gathering &amp; Small Trade Fair – Invitation</title>
<link rel="stylesheet" href="https://fonts.googleapis.com/css2?family=Roboto+Slab:wght@300;400;500&display=swap">
<style>
  :root {
    --sky: #00adef;
    --navy: #283891;
    --ink: #2e3192;
    --orange: #f7941d;
    --green: #39b54a;
    --white: #ffffff;
    --mist: #d6daf0;
    --page: #ffffff;
  }
  * { box-sizing: border-box; margin: 0; padding: 0; }
  html, body {
    width: 1200px; height: 809px; overflow: hidden;
    background: var(--page);
    font-family: "Roboto Slab", Georgia, serif;
  }
  .sheet { position: relative; width: 1200px; height: 809px; }

  .invite {
    position: absolute; top: 56px;
    width: 516px; height: 693px;
    border-radius: 24px;
    overflow: hidden;
    text-align: center;
  }
  .invite--sky { left: 49px; background: var(--sky); color: var(--ink); }
  .invite--navy { left: 642px; background: var(--navy); color: var(--mist); }

  .stripe { position: absolute; top: 138px; width: 13px; height: 172px; display: flex; flex-direction: column; }
  .stripe span { flex: 1; }
  .stripe--left { left: 0; }
  .stripe--right { right: 0; }

  .seal {
    position: absolute; left: 202px; top: 47px;
    width: 130px; height: 130px; border-radius: 50%;
    background: var(--white);
    display: flex; flex-direction: column; align-items: center; justify-content: center;
    color: var(--navy); font-weight: 500; line-height: 1.15;
  }
  .seal__name { font-size: 9px; letter-spacing: .02em; }
  .seal__sub { font-size: 6px; letter-spacing: .14em; text-transform: uppercase; }

  .scene {
    position: absolute; left: 107px; top: 228px; width: 320px; height: 70px;
    border-radius: 6px;
    z-index: 1;
  }
  .invite--sky .scene { background: rgba(255,255,255,.85); }
  .invite--navy .scene {
    background: linear-gradient(180deg, var(--sky) 0%, var(--sky) 22%, var(--orange) 30%, var(--orange) 68%, var(--green) 76%, var(--green) 100%);
  }

  .tagline { position: absolute; left: 0; top: 0; width: 516px; height: 240px; z-index: 2; }
  .tagline text { font-family: "Roboto Slab", Georgia, serif; font-size: 11.5px; font-weight: 400; fill: var(--white); }

  .line { position: absolute; left: 0; width: 100%; }
  .intro { top: 333px; font-size: 11.5px; font-weight: 300; }
  .invite--sky .intro { color: var(--ink); }
  .title { top: 356px; font-size: 28px; font-weight: 500; line-height: 34px; }
  .invite--sky .title { color: var(--white); }
  .invite--navy .title { color: var(--orange); }
  .date { top: 428px; font-size: 16.5px; font-weight: 500; }

  .rule { position: absolute; left: 191px; width: 144px; height: 1px; }
  .invite--sky .rule { background: var(--white); }
  .invite--navy .rule { background: #6b74b6; }
  .rule--top { top: 467px; }
  .rule--bottom { top: 563px; }

  .details { top: 485px; font-size: 14px; font-weight: 400; line-height: 22px; }
  .details .soft { font-weight: 300; }

  .closing { top: 594px; font-size: 11.5px; font-weight: 400; }
  .invite--navy .closing { color: var(--orange); }

  .rsvp {
    position: absolute; left: 171px; width: 183px; height: 23px;
    background: var(--white); color: #222;
    font-size: 8.5px; line-height: 23px;
  }
  .invite--sky .rsvp { top: 637px; }
  .invite--navy .rsvp { top: 625px; }
</style>
</head>
<body>
<main class="sheet">

  <section class="invite invite--sky">
    <div class="stripe stripe--left">
      <span style="background:var(--navy)"></span><span style="background:var(--green)"></span>
      <span style="background:var(--orange)"></span><span style="background:var(--white)"></span>
    </div>
    <div class="stripe stripe--right">
      <span style="background:var(--white)"></span><span style="background:var(--orange)"></span>
      <span style="background:var(--green)"></span><span style="background:var(--navy)"></span>
    </div>
    <div class="seal">
      <span class="seal__name">HARBORLINE CHAMBER</span>
      <span class="seal__sub">of commerce &amp; tourism</span>
    </div>
    <div class="scene" role="img" aria-label="Banquet table with two chairs, white silhouette"></div>
    <svg class="tagline" viewBox="0 0 516 240" aria-hidden="true">
      <path id="arcSky" d="M130 212 Q265 186 400 212" fill="none"/>
      <text><textPath href="#arcSky" startOffset="50%" text-anchor="middle">Bridging a gap for a better &amp; prosperous future</textPath></text>
    </svg>
    <p class="line intro">The Board of Directors and staff cordially invite you to attend the</p>
    <h1 class="line title">82nd Annual Gathering &amp;<br>Small Trade Fair</h1>
    <p class="line date">Monday, January 28, 2019</p>
    <div class="rule rule--top"></div>
    <p class="line details">• 5:30 P.M. Social &nbsp;• 6:00 P. M. Dinner<br><span class="soft">at</span> Eastvale Chapel, 4819 Carson T<br>Hale Hwy S, Whiteville</p>
    <div class="rule rule--bottom"></div>
    <p class="line closing">lets make this meeting a grand success.</p>
    <p class="rsvp">Please RSVP by January 21, 2019</p>
  </section>

  <section class="invite invite--navy">
    <div class="seal">
      <span class="seal__name">HARBORLINE CHAMBER</span>
      <span class="seal__sub">of commerce &amp; tourism</span>
    </div>
    <div class="scene" role="img" aria-label="Banquet table in blue, orange and green with two white chairs"></div>
    <svg class="tagline" viewBox="0 0 516 240" aria-hidden="true">
      <path id="arcNavy" d="M130 212 Q265 186 400 212" fill="none"/>
      <text><textPath href="#arcNavy" startOffset="50%" text-anchor="middle">Bridging a gap for a better &amp; prosperous future</textPath></text>
    </svg>
    <p class="line intro">The Board of Directors and staff cordially invite you to attend the</p>
    <h1 class="line title">82nd Annual Gathering &amp;<br>Small Trade Fair</h1>
    <p class="line date">Monday, January 28, 2019</p>
    <div class="rule rule--top"></div>
    <p class="line details">• 5:30 P.M. Social &nbsp;• 6:00 P. M. Dinner<br><span class="soft">at</span> Eastvale Chapel, 4819 Carson T<br>Hale Hwy S, Whiteville</p>
    <div class="rule rule--bottom"></div>
    <p class="line closing">lets make this meeting a grand success.</p>
    <p class="rsvp">Please RSVP by January 21, 2019</p>
  </section>

</main>
</body>
</html>
```